Certified Public Accountant specializing in tax preparation.

I need a business card designed that conveys knowledgeability, trustworthiness and competency. I am a licensed CPA and hold a Master's in taxation. As this is a personal service business, I would like to include my picture on the card.

```html
<!DOCTYPE html>
<html lang="en">
<head>
<meta charset="utf-8">
<title>Licensed CPA Business Card</title>
<link rel="stylesheet" href="https://fonts.googleapis.com/css2?family=Cinzel:wght@600&family=Crimson+Text:ital,wght@0,400;1,400&display=swap">
<style>
  :root {
    --backdrop: #e6e4e5;
    --card-white: #ffffff;
    --card-black: #1f1a1c;
    --lilac: #c8a8c9;
    --dot-pink: #c99cbd;
    --ink: #1a1718;
    --light-ink: #f2eef0;
    --photo-warm: #b98a6e;
    --photo-dark: #4a3430;
  }
  html, body {
    margin: 0;
    width: 1200px;
    height: 900px;
    overflow: hidden;
    background: var(--backdrop);
  }
  .canvas {
    position: relative;
    width: 1200px;
    height: 900px;
  }
  .card {
    position: absolute;
    left: 337px;
    width: 525px;
    height: 300px;
    border-radius: 22px;
    overflow: hidden;
    box-shadow: 0 6px 18px rgba(0,0,0,0.18);
  }
  .card--front { top: 110px; background: var(--card-white); }
  .card--back { top: 490px; background: var(--card-black); }
  .card svg { display: block; }
  .name {
    font-family: "Cinzel", serif;
    font-weight: 600;
    font-size: 27px;
    fill: var(--ink);
  }
  .title {
    font-family: "Cinzel", serif;
    font-weight: 600;
    font-size: 13px;
    letter-spacing: 0.6px;
    fill: var(--ink);
  }
  .address {
    font-family: "Crimson Text", serif;
    font-size: 18px;
    fill: var(--ink);
  }
  .contact {
    font-family: "Crimson Text", serif;
    font-size: 17px;
    fill: var(--light-ink);
  }
  .contact .number { font-size: 20px; }
  .website {
    font-family: "Crimson Text", serif;
    font-style: italic;
    font-size: 34px;
    fill: var(--light-ink);
  }
  .dots {
    stroke: var(--dot-pink);
    stroke-width: 3;
    stroke-linecap: round;
    stroke-dasharray: 0 9;
  }
</style>
</head>
<body>
<main class="canvas">

  <section class="card card--front" aria-label="Card front">
    <svg width="525" height="300" viewBox="0 0 525 300">
      <defs>
        <radialGradient id="portrait-tone" cx="45%" cy="45%" r="60%">
          <stop offset="0%" stop-color="var(--photo-warm)"/>
          <stop offset="100%" stop-color="var(--photo-dark)"/>
        </radialGradient>
      </defs>
      <polygon class="lilac-corner" points="0,0 255,0 0,140" fill="var(--lilac)"/>
      <polygon class="contact-band" points="0,168 120,222 525,222 525,300 0,300" fill="var(--card-black)"/>
      <circle class="portrait-ring" cx="138" cy="92" r="74" fill="var(--card-white)"/>
      <circle class="portrait" cx="138" cy="92" r="64" fill="url(#portrait-tone)" role="img" aria-label="Portrait photo of the accountant"/>

      <text class="name" x="500" y="62" text-anchor="end">Your Name</text>
      <text class="title" x="500" y="80" text-anchor="end">Licensed CPA</text>

      <line class="dots" x1="232" y1="104" x2="500" y2="104"/>

      <text class="address" x="242" y="140">4120 N. Linden Avenue</text>
      <text class="address" x="242" y="163">Maple Falls, NE 68990</text>

      <text class="contact" x="505" y="252" text-anchor="end">Direct <tspan class="number">123.456.7890</tspan> | Main <tspan class="number">123.456.7890</tspan></text>
      <text class="contact" x="505" y="277" text-anchor="end">emailaddress@site.com | <tspan font-style="italic">www.website.com</tspan></text>
    </svg>
  </section>

  <section class="card card--back" aria-label="Card back">
    <svg width="525" height="300" viewBox="0 0 525 300">
      <line class="dots" x1="205" y1="112" x2="320" y2="112"/>
      <text class="website" x="262.5" y="160" text-anchor="middle">www.website.com</text>
      <line class="dots" x1="205" y1="190" x2="320" y2="190"/>
    </svg>
  </section>

</main>
</body>
</html>
```